Gentleman's grooming products require a business card

I need a business card that incorporates the logo [ or parts of ] that we had Pixel Hive design for us as uploaded.

We sell online, mens grooming products including moustache waxes, beard oils and shaving accessories.
We want a card that is classy, professional and a card that shouts mens products.

Target Market(s)

Young professional male market

Industry/Entity Type

Business

Contact Information for Business Card

Ross and Edith Carwell
Lather and Lore
Purveyors of gentleman's stiffeners and grooming requisites
M :0418529647
E : ross@latherandlore.com.au
E : edith@latherandlore.com.au
E : sales@theblokesbalmery.com.au

W : www.latherandlore.com.au

Requirements
Must have
• Class
Nice to have
• Professionalism

```html
<!DOCTYPE html>
<html lang="en">
<head>
<meta charset="utf-8">
<title>Lather and Lore — Business Card</title>
<link href="https://fonts.googleapis.com/css2?family=Open+Sans:wght@400;600&display=swap" rel="stylesheet">
<style>
  :root {
    --backdrop: #cfcfcf;
    --card-dark: #3a3a3a;
    --card-light: #ffffff;
    --ink-light: #ffffff;
    --ink-dark: #3a3a3a;
    --ink-name: #6e6e6e;
    --icon-box: #7a7a7a;
    --badge-fill: #5a5a5a;
    --rule: rgba(255,255,255,0.85);
  }
  * { box-sizing: border-box; margin: 0; padding: 0; }
  html, body {
    width: 1200px; height: 800px; overflow: hidden;
    background: var(--backdrop);
    font-family: "Open Sans", Arial, sans-serif;
  }
  .stage {
    width: 1200px; height: 800px;
    display: flex; align-items: center; justify-content: center;
  }
  .business-card {
    width: 900px; height: 514px;
    background: var(--card-light);
    box-shadow: 0 12px 30px rgba(0,0,0,0.18);
    display: flex; flex-direction: column;
  }
  .brand-panel {
    height: 300px;
    background: var(--card-dark);
    position: relative;
    color: var(--ink-light);
  }
  .rule-top {
    position: absolute; left: 380px; right: 90px; top: 58px;
    height: 1px; background: var(--rule);
  }
  .brand-badge {
    position: absolute; left: 300px; top: 58px;
    width: 96px; height: 96px;
    background: var(--badge-fill);
    border: 1.5px solid var(--rule);
  }
  .brand-name {
    position: absolute; left: 230px; top: 150px;
    font-size: 54px; font-weight: 400; line-height: 1;
    color: var(--ink-light);
    letter-spacing: 0.5px;
    white-space: nowrap;
  }
  .rule-bottom {
    position: absolute; left: 200px; right: 180px; top: 220px;
    height: 1px; background: var(--rule);
  }
  .brand-tagline {
    position: absolute; left: 200px; right: 180px; top: 232px;
    text-align: center;
    font-size: 12px; font-weight: 400;
    text-transform: uppercase; letter-spacing: 2px;
    color: var(--ink-light);
    white-space: nowrap;
  }
  .contact-panel {
    flex: 1;
    display: flex; justify-content: space-between; align-items: flex-start;
    padding: 14px 40px 0 48px;
  }
  .owner-names {
    margin-top: 62px;
    font-size: 26px; font-weight: 600;
    color: var(--ink-name);
  }
  .contact-list { list-style: none; text-align: right; }
  .contact-item {
    display: flex; align-items: center; justify-content: flex-end; gap: 12px;
    font-size: 17px; line-height: 38px; color: var(--ink-dark);
  }
  .contact-icon { width: 20px; height: 20px; flex: none; }
</style>
</head>
<body>
<main class="stage">
  <article class="business-card">
    <header class="brand-panel">
      <div class="rule-top"></div>
      <div class="brand-badge" role="img" aria-label="Brand badge emblem"></div>
      <span class="brand-name">Lather and Lore</span>
      <div class="rule-bottom"></div>
      <p class="brand-tagline">Merchants of fine beard balms and shaving essentials</p>
    </header>
    <section class="contact-panel">
      <p class="owner-names">Ross and Edith Carwell</p>
      <ul class="contact-list">
        <li class="contact-item">0418529647
          <svg class="contact-icon" viewBox="0 0 20 20" aria-hidden="true">
            <path d="M5 3 L8 3 L9 7 L7 8.5 Q8.5 11.5 11.5 13 L13 11 L17 12 L17 15 Q16 17 13 16.5 Q5 14 3.5 6 Q3.5 3.5 5 3 Z" fill="var(--icon-box)"/>
          </svg>
        </li>
        <li class="contact-item">ross@latherandlore.com.au
          <svg class="contact-icon" viewBox="0 0 20 20" aria-hidden="true">
            <rect width="20" height="20" rx="2" fill="var(--icon-box)"/>
            <rect x="4" y="6" width="12" height="8" fill="none" stroke="#fff" stroke-width="1.3"/>
            <path d="M4 6 L10 11 L16 6" fill="none" stroke="#fff" stroke-width="1.3"/>
          </svg>
        </li>
        <li class="contact-item">edith@latherandlore.com.au
          <svg class="contact-icon" viewBox="0 0 20 20" aria-hidden="true">
            <rect width="20" height="20" rx="2" fill="var(--icon-box)"/>
            <rect x="4" y="6" width="12" height="8" fill="none" stroke="#fff" stroke-width="1.3"/>
            <path d="M4 6 L10 11 L16 6" fill="none" stroke="#fff" stroke-width="1.3"/>
          </svg>
        </li>
        <li class="contact-item">sales@theblokesbalmery.com.au
          <svg class="contact-icon" viewBox="0 0 20 20" aria-hidden="true">
            <rect width="20" height="20" rx="2" fill="var(--icon-box)"/>
            <rect x="4" y="6" width="12" height="8" fill="none" stroke="#fff" stroke-width="1.3"/>
            <path d="M4 6 L10 11 L16 6" fill="none" stroke="#fff" stroke-width="1.3"/>
          </svg>
        </li>
        <li class="contact-item">www.latherandlore.com.au
          <svg class="contact-icon" viewBox="0 0 20 20" aria-hidden="true">
            <circle cx="10" cy="10" r="9" fill="var(--icon-box)"/>
            <circle cx="10" cy="10" r="5.5" fill="none" stroke="#fff" stroke-width="1.2"/>
            <ellipse cx="10" cy="10" rx="2.3" ry="5.5" fill="none" stroke="#fff" stroke-width="1.2"/>
            <line x1="4.5" y1="10" x2="15.5" y2="10" stroke="#fff" stroke-width="1.2"/>
          </svg>
        </li>
      </ul>
    </section>
  </article>
</main>
</body>
</html>
```